Business Card for TVK, logo files already created

Please, can you assist with creating a Business card the TVK graphics which are already listed on www.brinmoretech.example
The business card should be modern and upmarket, textured designs are welcome. Please feel free to express yourself and be very bold with your design.

Target Market(s)

Cyber Security

Industry/Entity Type

Information Technology

Contact Information for Business Card

Company Name
Name
Title
Mobile
Fax or Tel
email
url

Font styles to use
Serif
Sans Serif

Colors
3277b5
85acd3
ffffff

```html
<!DOCTYPE html>
<html lang="en">
<head>
<meta charset="utf-8">
<title>TVK Business Card</title>
<link href="https://fonts.googleapis.com/css2?family=Montserrat:wght@400;500;700;800&display=swap" rel="stylesheet">
<style>
  :root {
    --blue-deep: #143a9c;
    --blue-mid: #1f47a8;
    --blue-light: #3a5fb0;
    --white: #ffffff;
    --paper: #f6f6f6;
    --backdrop: #1c1c1c;
  }
  * { margin: 0; padding: 0; box-sizing: border-box; }
  html, body { width: 1200px; height: 900px; overflow: hidden; }
  body {
    background: var(--backdrop);
    font-family: "Montserrat", Arial, sans-serif;
    position: relative;
  }
  .card {
    position: absolute;
    left: 250px;
    width: 700px;
    height: 400px;
    overflow: hidden;
    box-shadow: 0 10px 30px rgba(0,0,0,.55);
  }
  .card--front { top: 40px; background: linear-gradient(200deg, var(--blue-light) 0%, var(--blue-mid) 45%, var(--blue-deep) 100%); }
  .card--back { top: 460px; background: var(--paper); }

  /* front */
  .front-band { position: absolute; inset: 0; }
  .brand-lockup {
    position: absolute;
    left: 0; right: 0; top: 48px;
    text-align: center;
    color: var(--white);
    white-space: nowrap;
  }
  .brand-mark {
    font-weight: 800;
    font-size: 96px;
    line-height: 1;
    letter-spacing: 6px;
  }
  .brand-name {
    font-weight: 800;
    font-size: 26px;
    letter-spacing: 3px;
    margin-top: 6px;
  }
  .brand-tagline {
    display: inline-block;
    margin-top: 10px;
    padding-top: 8px;
    border-top: 2px solid currentColor;
    font-weight: 500;
    font-size: 13px;
    letter-spacing: 2.5px;
  }
  .front-url {
    position: absolute;
    left: 0; right: 0; top: 258px;
    text-align: center;
    color: var(--white);
    font-size: 14px;
    font-weight: 500;
    letter-spacing: 4px;
  }

  /* back */
  .back-art { position: absolute; inset: 0; }
  .back-lockup {
    position: absolute;
    left: 24px; top: 66px;
    width: 260px;
    text-align: center;
    color: var(--blue-mid);
    white-space: nowrap;
  }
  .back-lockup .brand-mark { font-size: 72px; letter-spacing: 4px; }
  .back-lockup .brand-name { font-size: 15px; letter-spacing: 1px; }
  .back-lockup .brand-tagline { font-size: 10px; letter-spacing: 1.2px; padding-top: 6px; margin-top: 8px; }

  .contact {
    position: absolute;
    right: 40px; top: 86px;
    text-align: right;
    color: var(--white);
  }
  .contact-name { font-weight: 700; font-size: 26px; }
  .contact-title { font-weight: 400; font-size: 15px; margin-top: 2px; }
  .contact-address { font-weight: 700; font-size: 13px; margin-top: 22px; }
  .contact-line {
    display: flex; justify-content: flex-end; align-items: center; gap: 10px;
    font-size: 15px; margin-top: 12px;
  }
  .contact-line svg { width: 16px; height: 16px; fill: var(--white); }
</style>
</head>
<body>

<section class="card card--front">
  <svg class="front-band" width="700" height="400" viewBox="0 0 700 400" aria-hidden="true">
    <rect x="0" y="306" width="700" height="94" fill="#f6f6f6"/>
    <rect x="0" y="292" width="700" height="2" fill="#ffffff"/>
    <rect x="0" y="298" width="700" height="2" fill="#ffffff"/>
  </svg>
  <div class="brand-lockup">
    <div class="brand-mark">TVK</div>
    <div class="brand-name">BRINMORE TECHNOLOGIES</div>
    <div class="brand-tagline">PROACTIVE - ADAPTIVE DEFENSE</div>
  </div>
  <div class="front-url">www.brinmoretech.example</div>
</section>

<section class="card card--back">
  <svg class="back-art" width="700" height="400" viewBox="0 0 700 400" aria-hidden="true">
    <defs>
      <linearGradient id="backBlue" x1="1" y1="0" x2="0" y2="1">
        <stop offset="0" stop-color="#3a5fb0"/>
        <stop offset="0.5" stop-color="#1f47a8"/>
        <stop offset="1" stop-color="#143a9c"/>
      </linearGradient>
    </defs>
    <polygon points="440,0 700,0 700,400 290,400" fill="url(#backBlue)"/>
    <polygon points="422,0 428,0 278,400 272,400" fill="#1f47a8"/>
    <polygon points="410,0 414,0 264,400 260,400" fill="#1f47a8"/>
  </svg>
  <div class="back-lockup">
    <div class="brand-mark">TVK</div>
    <div class="brand-name">BRINMORE TECHNOLOGIES</div>
    <div class="brand-tagline">PROACTIVE - ADAPTIVE DEFENSE</div>
  </div>
  <div class="contact">
    <div class="contact-name">Dana Whitfield</div>
    <div class="contact-title">Chief Executive Officer</div>
    <div class="contact-address">415 Harbor Lane, Suite 210, NC 27500</div>
    <div class="contact-line">555.010.2143
      <svg viewBox="0 0 16 16" aria-hidden="true"><path d="M3 2h3l1.5 3.5-2 1.2a8 8 0 0 0 3.8 3.8l1.2-2L14 10v3a1 1 0 0 1-1 1A11 11 0 0 1 2 3a1 1 0 0 1 1-1z"/></svg>
    </div>
    <div class="contact-line">555.010.8870
      <svg viewBox="0 0 16 16" aria-hidden="true"><rect x="4" y="1" width="8" height="4"/><rect x="1" y="6" width="14" height="6" rx="1"/><rect x="4" y="10" width="8" height="5" fill="#1f47a8" stroke="#fff" stroke-width="1.5"/></svg>
    </div>
    <div class="contact-line">contact@brinmoretech.example
      <svg viewBox="0 0 16 16" aria-hidden="true"><rect x="1" y="3" width="14" height="10"/><path d="M1 3l7 6 7-6" fill="none" stroke="#1f47a8" stroke-width="1.5"/></svg>
    </div>
  </div>
</section>

</body>
</html>
```